Flyer für Bürgerenergiegemeinschaft
Zielgruppe
Als Bürgerenergiegemeinschaft sind wir für unsere Bürgerinnen und Bürger die erste Anlaufstelle wenn es um sauberen regionalen erneuerbaren Strom geht. Mehr Infos unter www.kwl-rax.example
Aufgabenstellung
Ziel soll ein Falzflyer DL (220x110mm) mit Wickelfalz von Drucklo (https://www.drucklomat.example/marketingmaterial/falzflyer) sein. Bitte daher die Designrichtlinien von Drucklo beachten. Ausgefaltet hat der Flyer dann 297x210mm, gefaltet 99x210mm. Somit sind 6 kleine Seiten zu befüllen.
Auf diesen 6 Seiten soll der Inhalt unserer Webseite www.kwl-rax.example im gleichen Look übersichtlich aufbereitet werden.
Auf der gefalteten Rückseite sollen im unterne Bereich die nicht ausgefüllten Felder des Online-Rechners sein,
damit man im Kundengespräch die Werte die der Rechner ausgibt auf den Flyer niederschreiben kann den der Kunde dann mitbekommt.
Bilder können von der Webseite geladen werden oder von uns zur Verfügung gestellt werden.

```html
<!DOCTYPE html>
<html lang="de">
<head>
<meta charset="utf-8">
<title>KWLRAX Falzflyer</title>
<link href="https://fonts.googleapis.com/css2?family=Poppins:wght@400;500;600;700;800&display=swap" rel="stylesheet">
<style>
:root{
  --blue:#1b8fd8;
  --navy:#21407c;
  --navy-dark:#1a3468;
  --ink:#1e2f55;
  --text:#3b4660;
  --line:#1d3f7a;
  --paper:#ffffff;
  --bg:#e6e7e9;
}
*{box-sizing:border-box;margin:0;padding:0}
html,body{width:802px;height:1200px;overflow:hidden}
body{background:var(--bg);font-family:"Poppins",Arial,sans-serif;color:var(--text);position:relative}
.spread{position:absolute;left:21px;width:760px;height:537px;background:var(--paper);display:flex;box-shadow:0 2px 8px rgba(0,0,0,.18)}
.spread--outer{top:40px}
.spread--inner{top:623px}
.panel{position:relative;width:253.33px;height:100%;overflow:hidden}
.panel + .panel{border-left:1px solid #eef0f3}
.pad{padding:18px 18px 0}
.kicker{font-size:6.5px;color:var(--blue);text-transform:uppercase;letter-spacing:.2px}
.title{font-size:12px;font-weight:700;color:var(--ink);line-height:1.15;margin-top:2px}
.body-copy{font-size:6.6px;line-height:1.45;margin-top:9px}
.photo{position:absolute;left:0;width:100%}
.footer{position:absolute;left:0;bottom:0;width:100%;height:52px;background:var(--navy);color:#fff}
/* about panel */
.perks{margin-top:12px;border:1px solid #c9d6ea;padding:8px 10px;display:grid;grid-template-columns:1fr 1fr;gap:6px 8px;font-size:6.3px}
.perk{display:flex;align-items:center;gap:4px}
.dot{width:7px;height:7px;border-radius:50%;background:var(--blue);flex:none;position:relative}
.dot::after{content:"";position:absolute;left:2px;top:1.5px;width:2px;height:3px;border:solid #fff;border-width:0 1px 1px 0;transform:rotate(45deg)}
.mail-band{margin:14px 0 0;background:var(--blue);color:#fff;height:44px;display:flex;align-items:center;gap:12px;padding:0 18px;font-size:6.6px;line-height:1.35}
.mail-band b{font-size:7.5px;font-weight:700}
.mail-icon{width:22px;height:16px;flex:none}
.board{display:flex;gap:6px;margin-top:8px}
.member{flex:1;font-size:4.8px;color:var(--ink);line-height:1.3}
.member .pic{height:46px;background:linear-gradient(180deg,#d9cfa2,#5d5f66)}
.member small{display:block;color:var(--blue);font-size:4.2px}
.contact{padding:12px 18px;font-size:6.8px;font-weight:600;line-height:1.7}
.contact .row{display:flex;align-items:center;gap:5px}
.pin{width:6px;height:6px;border-radius:50%;background:var(--blue)}
/* calculator panel */
.calc{margin:14px 10px 0;border:1px solid #c5d3e8;padding:8px 9px 9px}
.calc .kicker{font-size:5.6px;color:var(--ink)}
.calc .title{font-size:7px}
.check-row{display:flex;gap:18px;margin-top:7px;font-size:6px}
.check-row .perk{align-items:flex-start}
.calc p{font-size:5.3px;line-height:1.4;margin-top:6px}
.field{margin-top:6px;font-size:6.3px;color:var(--ink)}
.field .box{margin-top:2px;height:10px;border:1px solid #b9c8df;font-size:4.4px;color:#8c98ae;padding:1.5px 4px}
.field--result{margin-top:7px;height:11px;background:var(--blue);color:#fff;font-size:6px;text-align:center;line-height:11px}
.notes{margin:12px 10px 0;font-size:6px;font-weight:600;color:var(--ink)}
/* cover */
.brand{display:flex;align-items:center;gap:6px;justify-content:center}
.brand-mark{width:14px;height:14px;border-radius:50%;background:var(--blue)}
.brand-name{font-size:19px;font-weight:800;color:var(--blue);letter-spacing:.5px}
.cover-rule{height:4px;background:var(--blue);margin:0 8px}
.cover-sub{text-align:center;font-size:6.3px;color:var(--ink);letter-spacing:.3px;line-height:1.35;margin-top:6px}
.cover-head{text-align:center;font-size:14px;font-weight:800;color:var(--navy);line-height:1.15;margin-top:6px}
.stats{display:flex;margin:12px 17px 0;height:64px}
.stat{flex:1;color:#fff;text-align:center;padding-top:6px;font-size:5.3px}
.stat:nth-child(odd){background:var(--blue)}
.stat:nth-child(2){background:var(--navy)}
.stat-icon{width:15px;height:15px;border-radius:50%;border:1.5px solid #fff;margin:0 auto 4px}
.stat strong{display:block;font-size:14px;font-weight:800;line-height:1.05}
.stat strong.small{font-size:8px;line-height:1.2;margin-top:1px}
.url{text-align:center;line-height:52px;font-size:10px;font-weight:700}
/* inner left */
.features{margin-top:12px;display:flex;flex-direction:column;gap:11px}
.feature{display:flex;gap:9px}
.icon-sq{width:18px;height:18px;background:var(--blue);flex:none;display:flex;align-items:center;justify-content:center}
.feature h4{font-size:6.8px;font-weight:700;color:var(--ink)}
.feature p{font-size:5.5px;line-height:1.4}
/* services */
.services{margin:12px 14px 0;display:grid;grid-template-columns:1fr 1fr;gap:11px 8px}
.svc{position:relative;border:1px solid var(--line);height:24px;font-size:5.3px;font-weight:700;color:var(--ink);text-align:center;padding-top:13px}
.svc::before{content:"";position:absolute;left:50%;top:-7px;width:13px;height:13px;margin-left:-6.5px;background:var(--blue);transform:rotate(45deg)}
.svc--wide{grid-column:1 / span 2;width:50%;justify-self:center}
.inner-mail{position:absolute;left:0;right:0;bottom:52px}
.logo-foot{position:absolute;bottom:0;left:0;right:0;height:52px;display:flex;align-items:center;justify-content:center}
/* join */
.steps{margin-top:12px;display:flex;flex-direction:column;gap:12px}
.price{text-align:center;font-size:8px;font-weight:700;padding-top:13px;line-height:1.35}
</style>
</head>
<body>

<!-- outer side -->
<section class="spread spread--outer">
  <article class="panel panel--about">
    <div class="pad">
      <div class="kicker">Über uns</div>
      <h2 class="title" style="font-size:10px">Bürgerenergiegemeinschaft<br>St. Veitsberg an der Lauter</h2>
      <p class="body-copy">Als Bürgerenergiegemeinschaft sind wir für unsere Bürgerinnen und Bürger die erste Anlaufstelle wenn es um sauberen regionalen erneuerbaren Strom geht.</p>
      <div class="perks">
        <span class="perk"><i class="dot"></i>Grüne Energie</span>
        <span class="perk"><i class="dot"></i>Faire Preise</span>
        <span class="perk"><i class="dot"></i>Regional produziert</span>
        <span class="perk"><i class="dot"></i>Für jeden</span>
      </div>
    </div>
    <div class="mail-band">
      <svg class="mail-icon" viewBox="0 0 22 16"><rect x="1" y="1" width="20" height="14" fill="none" stroke="#fff" stroke-width="1.5"/><path d="M1 1 L11 9 L21 1" fill="none" stroke="#fff" stroke-width="1.5"/></svg>
      <div>Schicken Sie uns gerne eine E-Mail<br>wenn Sie Fragen haben<br><b>info@kwl-rax.example</b></div>
    </div>
    <div class="pad" style="padding-top:12px">
      <div class="kicker">Vereinsvorstand</div>
      <h3 class="title" style="font-size:7.5px">Gerne helfen wir unseren Mitgliedern<br>bei Fragen rund um die KWLRAX</h3>
      <div class="board">
        <div class="member"><div class="pic" role="img" aria-label="Porträtfoto Vorstandsmitglied"></div>Ing. Lukas Brenner<small>Obmann</small></div>
        <div class="member"><div class="pic" role="img" aria-label="Porträtfoto Vorstandsmitglied"></div>Ing. Tobias Hollerer MSc<small>Kassier</small></div>
        <div class="member"><div class="pic" role="img" aria-label="Porträtfoto Vorstandsmitglied"></div>Ing. Martin Gstettner<small>Schriftführer</small></div>
      </div>
    </div>
    <div class="photo" style="top:395px;height:90px;background:linear-gradient(180deg,#9fc3e6,#5a6a80)" role="img" aria-label="Foto eines Umspannwerks mit Hochspannungsanlagen"></div>
    <div class="footer contact">
      <div class="row"><i class="pin"></i>info@kwl-rax.example &nbsp;|&nbsp; <i class="pin"></i>www.kwl-rax.example</div>
      <div class="row"><i class="pin"></i>Lindenweg 12 3240 Veitsberg</div>
    </div>
  </article>

  <article class="panel panel--calculator">
    <div class="calc">
      <div class="kicker">Online Rechner</div>
      <h2 class="title">Dient zur einfachen Kostenabschätzung</h2>
      <div class="check-row">
        <span class="perk"><i class="dot"></i>Direkt-Ergebnis</span>
        <span class="perk"><i class="dot"></i>Komplett<br>unverbindlich</span>
      </div>
      <p>Wir stellen Ihnen hier eine einfache Möglichkeit zur Verfügung die Sinnhaftigkeit eines Beitritts in die BEG durchzurechnen.</p>
      <div class="field"><div class="box">Energiekosten Bezug</div></div>
      <div class="field"><div class="box">Auswählbare Beispiele</div></div>
      <div class="field">Energiekosten Bezug:<div class="box">Jahresabrechnungskosten in € brutto</div></div>
      <div class="field">Energiemenge Bezug:<div class="box">kWh pro Jahr</div></div>
      <div class="field">Einspeisevergütung:<div class="box">Cent/kWh netto</div></div>
      <div class="field">Einspeisevergütung:<div class="box">kWh pro Jahr</div></div>
      <div class="field--result">Einspeisevergütung</div>
      <div class="field"><div class="box">Ergebnis</div></div>
    </div>
    <div class="notes">persönliche Notizen:</div>
  </article>

  <article class="panel panel--cover">
    <div class="photo" style="top:0;height:218px;background:linear-gradient(180deg,#a9c3dd 0%,#7d9a6a 45%,#8a4a3a 75%,#5d6b45 100%)" role="img" aria-label="Luftbild eines Dorfes mit Kirche und Hügeln"></div>
    <div style="position:absolute;top:228px;left:0;right:0">
      <div class="brand"><span class="brand-mark"></span><span class="brand-name">KWLRAX</span></div>
      <div class="cover-rule"></div>
      <div class="cover-sub">BÜRGERENERGIEGEMEINSCHAFT<br>ST. VEITSBERG AN DER LAUTER</div>
      <div class="cover-head">Regionaler Strom<br>für jeden!</div>
      <div class="stats">
        <div class="stat"><div class="stat-icon"></div>Zählpunkte<strong>20+</strong></div>
        <div class="stat"><div class="stat-icon"></div>PV Leistung<strong>&gt;100</strong>kWp</div>
        <div class="stat"><div class="stat-icon"></div>Verteilte Energie<strong class="small">Testphase</strong></div>
      </div>
    </div>
    <div class="footer url">www.kwl-rax.example</div>
  </article>
</section>

<!-- inner side -->
<section class="spread spread--inner">
  <article class="panel panel--why">
    <div class="pad">
      <div class="kicker">Warum sollten Sie bei uns Kunde werden?</div>
      <h2 class="title" style="font-size:9.5px">Wir helfen Ihnen Ihre Stromkosten zu senken und dabei etwas Gutes für die Umwelt zu tun</h2>
      <div class="features">
        <div class="feature"><span class="icon-sq"><svg width="11" height="11" viewBox="0 0 11 11"><circle cx="5.5" cy="5.5" r="2.5" fill="#fff"/><path d="M5.5 0v2M5.5 9v2M0 5.5h2M9 5.5h2" stroke="#fff"/></svg></span><div><h4>PV Anlagen Besitzer</h4><p>Als Anlagenbesitzer mit Einspeisung bekommen Sie bei uns bessere Preise als bei einer Einspeisung zum Marktpreis.</p></div></div>
        <div class="feature"><span class="icon-sq"><svg width="11" height="11" viewBox="0 0 11 11"><path d="M1 3h8l-2-2M10 8H2l2 2" fill="none" stroke="#fff" stroke-width="1.3"/></svg></span><div><h4>Stromverteilung neu durchdacht</h4><p>Der Strom bleibt innerhalb der Gemeinschaft und es ist somit jederzeit nachvollziehbar woher dieser kommt.</p></div></div>
        <div class="feature"><span class="icon-sq"><svg width="11" height="11" viewBox="0 0 11 11"><path d="M3 3a4 4 0 1 0 5 0" fill="none" stroke="#fff" stroke-width="1.3"/><path d="M5.5 1v4" stroke="#fff" stroke-width="1.3"/></svg></span><div><h4>Kunden ohne PV Anlage</h4><p>Durch die Energiegemeinschaft beziehen Sie grünen regionalen Strom zu reduzierten Kosten.</p></div></div>
        <div class="feature"><span class="icon-sq"><svg width="11" height="11" viewBox="0 0 11 11"><circle cx="3" cy="4" r="1.5" fill="#fff"/><circle cx="8" cy="4" r="1.5" fill="#fff"/><circle cx="5.5" cy="6" r="1.8" fill="#fff"/><path d="M2 10a3.5 3 0 0 1 7 0z" fill="#fff"/></svg></span><div><h4>Kleines Team</h4><p>Durch unsere schlanke Organisation kommen wir mit geringen Overhead-Kosten für den Strombezieher aus.</p></div></div>
      </div>
    </div>
    <div class="photo" style="top:330px;height:6px;background:var(--navy)"></div>
    <div class="photo" style="top:336px;bottom:0;background:linear-gradient(160deg,#e8e2d8,#b9a08a 55%,#6e5848)" role="img" aria-label="Foto einer Mutter mit Kind in der Küche"></div>
  </article>

  <article class="panel panel--services">
    <div class="pad">
      <div class="kicker">Unser Service für Sie</div>
      <h2 class="title" style="font-size:9.5px">Energiegemeinschaft auf<br>neuem Level</h2>
    </div>
    <div class="services">
      <div class="svc">Anmeldungen</div>
      <div class="svc">Transparenz</div>
      <div class="svc">SEPA Lastschrift</div>
      <div class="svc">Einspeisevertrag</div>
      <div class="svc">Bürgerenergiegemeinschaft</div>
      <div class="svc">Bezugsvertrag</div>
      <div class="svc">Energieeinspeisung</div>
      <div class="svc">Gemeinschaftskosten</div>
      <div class="svc svc--wide">Energieabnahme</div>
    </div>
    <div class="mail-band inner-mail">
      <svg class="mail-icon" viewBox="0 0 22 16"><rect x="1" y="1" width="20" height="14" fill="none" stroke="#fff" stroke-width="1.5"/><path d="M1 1 L11 9 L21 1" fill="none" stroke="#fff" stroke-width="1.5"/></svg>
      <div>Schicken Sie uns gerne eine E-Mail<br>wenn Sie Fragen haben<br><b>info@kwl-rax.example</b></div>
    </div>
    <div class="logo-foot"><div class="brand"><span class="brand-mark"></span><span class="brand-name">KWLRAX</span></div></div>
  </article>

  <article class="panel panel--join">
    <div class="photo" style="top:0;height:120px;background:linear-gradient(135deg,#f3f3f3,#cfcfcf 50%,#c89f85)" role="img" aria-label="Foto einer Hand, die einen Stecker in eine Steckdose steckt"></div>
    <div class="pad" style="position:absolute;top:138px;left:0;right:0">
      <div class="kicker">Beitritt in die Energiegemeinschaft</div>
      <h2 class="title" style="font-size:9.5px">Folgende Voraussetzungen<br>müssen für den Beitritt<br>erfüllt sein</h2>
      <div class="features steps">
        <div class="feature"><span class="icon-sq" style="transform:rotate(45deg);width:15px;height:15px;margin:2px"></span><div><h4>Netzgebiet</h4><p>Um Teil unserer KWLRAX zu werden müssen Sie im Regionalnetz angeschlossen sein.</p></div></div>
        <div class="feature"><span class="icon-sq" style="transform:rotate(45deg);width:15px;height:15px;margin:2px"></span><div><h4>Smart Meter + Opt-In</h4><p>Damit wir Ihre Einspeisung/Bezug erfassen können muss ein kommunikativer SmartMeter inkl. 15min Opt-In verbaut sein.</p></div></div>
        <div class="feature"><span class="icon-sq" style="transform:rotate(45deg);width:15px;height:15px;margin:2px"></span><div><h4>SmartMeter Portal</h4><p>Bestehender Login um uns die Freigabe auf Ihre Daten zu erteilen.</p></div></div>
      </div>
    </div>
    <div class="footer price">Preisstruktur/übersicht<br>(14,2,14 Cent)</div>
  </article>
</section>

</body>
</html>
```